Bright, Fun and hard to forget home inspection business card.

We need a Business card design for a new Home Inspection company. We are building a brand that is bright, fun and easy to remember.

Target Market(s)

Anyone involed in buying and selling of homes.

Industry/Entity Type

Home Inspection

Contact Information for Business Card

Colin Marlowe Owner/Inspector

Wedsite- PorchAndRafterCheck.example
Phone: 253-555-0187
Email- ColinMarlowe@mailbox.example
WA Lic # 4806

Requirements
Must have
• BRQV LOGO somewhere on card.

```html
<!DOCTYPE html>
<html lang="en">
<head>
<meta charset="utf-8">
<title>Home Inspections by Colin Marlowe – Business Card</title>
<link rel="stylesheet" href="https://fonts.googleapis.com/css2?family=Montserrat:wght@700;800&display=swap">
<style>
  :root {
    --sky-blue: #1577c0;
    --brand-red: #ed1c24;
    --ink-black: #111111;
    --ink-navy: #2b2466;
    --paper: #ffffff;
    --panel-edge: #1d2a3a;
  }
  html, body {
    margin: 0;
    padding: 0;
    overflow: hidden;
    background: var(--paper);
  }
  .card {
    position: relative;
    width: 966px;
    height: 1200px;
    background: var(--paper);
    font-family: "Montserrat", "Verdana", sans-serif;
    overflow: hidden;
  }
  .hero-panel {
    position: absolute;
    left: 0;
    top: 0;
    width: 964px;
    height: 555px;
    background: var(--sky-blue);
    border: 1px solid var(--panel-edge);
  }
  .mascot-art {
    position: absolute;
    left: 28px;
    top: 8px;
    width: 392px;
    height: 538px;
    background: linear-gradient(180deg, #ee2a30 0%, #e41b22 60%, #c9161c 100%);
  }
  .tagline {
    position: absolute;
    left: 420px;
    top: 78px;
    width: 540px;
    margin: 0;
    color: var(--paper);
    font-weight: 700;
    font-size: 74px;
    line-height: 96px;
    text-align: center;
  }
  .contact-frame {
    position: absolute;
    left: 0;
    top: 644px;
    width: 966px;
    height: 556px;
    background: var(--brand-red);
  }
  .name-box {
    position: absolute;
    left: 16px;
    top: 16px;
    width: 934px;
    height: 210px;
    background: var(--paper);
    text-align: center;
    color: var(--ink-black);
  }
  .business-name {
    margin: 17px 0 0;
    font-size: 87px;
    font-weight: 700;
    line-height: 1;
  }
  .owner-line {
    margin: 12px 0 0;
    font-size: 52px;
    font-weight: 700;
    line-height: 1.1;
  }
  .web-band {
    position: absolute;
    left: 16px;
    top: 241px;
    width: 934px;
    height: 84px;
    background: var(--sky-blue);
    color: var(--paper);
    font-size: 46px;
    font-weight: 700;
    line-height: 84px;
    text-align: center;
  }
  .details-box {
    position: absolute;
    left: 16px;
    top: 341px;
    width: 934px;
    height: 199px;
    background: var(--paper);
    color: var(--ink-navy);
  }
  .email {
    position: absolute;
    left: 18px;
    top: 64px;
    margin: 0;
    font-size: 38px;
    font-weight: 700;
  }
  .phone {
    position: absolute;
    left: 18px;
    top: 128px;
    margin: 0;
    font-size: 42px;
    font-weight: 700;
  }
  .license {
    position: absolute;
    left: 516px;
    top: 149px;
    margin: 0;
    font-size: 31px;
    font-weight: 700;
  }
  .cert-badge {
    position: absolute;
    left: 763px;
    top: 16px;
    width: 158px;
    height: 174px;
  }
</style>
</head>
<body>
  <main class="card">
    <section class="hero-panel">
      <div class="mascot-art" role="img" aria-label="Cartoon illustration of a red house character mascot"></div>
      <p class="tagline">How well do you really know your house?</p>
    </section>

    <section class="contact-frame">
      <div class="name-box">
        <h1 class="business-name">Home Inspections</h1>
        <p class="owner-line">by Colin Marlowe</p>
      </div>
      <div class="web-band">PorchAndRafterCheck.example</div>
      <div class="details-box">
        <p class="email">ColinMarlowe@mailbox.example</p>
        <p class="phone">Phone -253-555-0187</p>
        <p class="license">WA Lic # 4806</p>
        <svg class="cert-badge" viewBox="0 0 158 174" role="img" aria-label="Certification badge">
          <rect x="0" y="0" width="158" height="174" fill="#111111"/>
        </svg>
      </div>
    </section>
  </main>
</body>
</html>
```